Homemaking training schools needs a Business Card design

Designer, Hello!

No special requirements, good-looking enough.
--------------------------------------------------------------------------

Name: Marcus Liao
Chairman
Tel: 0574-57418263
Mobile: 13852247106
Email: kelvory@mailpond.com
Web: www.tqb2031.com
Add: No.258, LinfengJie, DaoyueQu, Ningbo, Zhejiang

LOGO
Ningbo TQB Homemaking Training School

Target Market(s)

pregnant women, mothers, infants, the elderly and families, including cleaning, cooking, nursing training.

Industry/Entity Type

Business

Contact Information for Business Card

Name: Marcus Liao
Chairman
Tel: 0574-57418263
Mobile: 13852247106
Email: kelvory@mailpond.com
Web: www.tqb2031.com

LOGO

Font styles to use
Serif
Sans Serif
Decorative

Requirements
Nice to have
• Feels: clean, specifications, safety, comfort, warmth and happiness.

```html
<!DOCTYPE html>
<html lang="en">
<head>
<meta charset="utf-8">
<title>TianQiaoBao Business Card</title>
<link href="https://fonts.googleapis.com/css2?family=Open+Sans:wght@400;600;700&display=swap" rel="stylesheet">
<style>
  :root {
    --backdrop: #3d3634;
    --card: #121212;
    --brand-blue: #2f8ad0;
    --accent-pink: #e3197f;
    --text-light: #f2f2f2;
    --silver: #c9c9c9;
    --rule: #8a8a8a;
  }
  * { margin: 0; padding: 0; box-sizing: border-box; }
  html, body { width: 1200px; height: 814px; overflow: hidden; }
  body {
    background: var(--backdrop);
    font-family: "Open Sans", Arial, sans-serif;
    position: relative;
  }
  .card {
    position: absolute;
    top: 249px;
    width: 540px;
    height: 316px;
    background: var(--card);
    box-shadow: 0 10px 28px rgba(0,0,0,.45);
  }
  .card--contact { left: 50px; }
  .card--brand { left: 610px; }

  /* contact side */
  .brand-lockup {
    position: absolute;
    left: 40px;
    top: 128px;
    width: 220px;
    text-align: center;
  }
  .brand-lockup__name {
    display: inline-flex;
    align-items: center;
    gap: 8px;
    font-size: 25px;
    font-weight: 700;
    color: var(--brand-blue);
    letter-spacing: -0.3px;
  }
  .brand-lockup__dot {
    width: 12px; height: 12px; border-radius: 50%;
    background: var(--accent-pink);
  }
  .brand-lockup__rule {
    height: 1px; background: var(--rule); margin: 6px 10px 4px;
  }
  .brand-lockup__tagline {
    font-size: 11px; color: var(--silver); letter-spacing: .5px;
  }
  .divider {
    position: absolute;
    left: 282px; top: 40px;
    width: 1px; height: 236px;
    background: linear-gradient(var(--rule), rgba(138,138,138,.2));
  }
  .contact {
    position: absolute;
    left: 302px; top: 44px;
    color: var(--text-light);
  }
  .contact__name { font-size: 19px; font-weight: 600; color: var(--brand-blue); }
  .contact__title { font-size: 12px; color: var(--accent-pink); margin-bottom: 8px; }
  .contact__address { font-size: 13px; line-height: 19px; }
  .contact__list { list-style: none; font-size: 13px; line-height: 19px; }
  .contact__item { display: flex; align-items: center; gap: 8px; }
  .contact__icon { width: 11px; height: 11px; flex: none; fill: var(--brand-blue); }
  .contact__item--plain { padding-left: 19px; }

  /* brand side */
  .hero {
    position: absolute;
    left: 0; right: 0; top: 118px;
    text-align: center;
  }
  .hero__name {
    display: inline-flex; align-items: center; gap: 10px;
    font-size: 40px; font-weight: 700; color: var(--silver);
  }
  .hero__dot { width: 16px; height: 16px; border-radius: 50%; background: var(--silver); }
  .hero__tagline { font-size: 14px; color: var(--silver); margin-top: 4px; letter-spacing: .6px; }
  .hero__web {
    position: absolute; left: 0; right: 0; top: 238px;
    text-align: center; font-size: 11px; color: var(--text-light);
    letter-spacing: 4px;
  }
</style>
</head>
<body>
  <section class="card card--contact">
    <div class="brand-lockup">
      <div class="brand-lockup__name"><span class="brand-lockup__dot"></span>TianQiaoBao</div>
      <div class="brand-lockup__rule"></div>
      <div class="brand-lockup__tagline">Training &amp; Services</div>
    </div>
    <div class="divider"></div>
    <div class="contact">
      <div class="contact__name">Marcus Liao</div>
      <div class="contact__title">Chairman</div>
      <ul class="contact__list">
        <li class="contact__item contact__item--plain">No.258, LinfengJie</li>
        <li class="contact__item contact__item--plain">DaoyueQu, Ningbo, Zhejiang</li>
        <li class="contact__item contact__item--plain">0574-57418263</li>
        <li class="contact__item">
          <svg class="contact__icon" viewBox="0 0 12 12"><path d="M2.5 0.8l2 2.2-1 1.3c.8 1.6 2 2.8 3.6 3.6l1.3-1 2.2 2-1.2 2.1C4.8 10.8 1.2 7.2.4 2z"/></svg>
          13852247106
        </li>
        <li class="contact__item">
          <svg class="contact__icon" viewBox="0 0 12 12"><path d="M0 2h12v8H0z M1 3l5 3.5L11 3z" fill-rule="evenodd"/></svg>
          kelvory@mailpond.com
        </li>
        <li class="contact__item">
          <svg class="contact__icon" viewBox="0 0 12 12"><circle cx="6" cy="6" r="6"/><path d="M0.5 6h11M6 0.5c-2.4 2.8-2.4 8.2 0 11M6 0.5c2.4 2.8 2.4 8.2 0 11" stroke="#121212" stroke-width=".8" fill="none"/></svg>
          www.tqb2031.com
        </li>
      </ul>
    </div>
  </section>

  <section class="card card--brand">
    <div class="hero">
      <div class="hero__name"><span class="hero__dot"></span>TianQiaoBao</div>
      <div class="hero__tagline">Training &amp; Services</div>
    </div>
    <div class="hero__web">www.tqb2031.com</div>
  </section>
</body>
</html>
```